Tiny Brookvale - Haircuts

Flyer - Tiny Brookvale is a independent kids clothes, babywear and toy shop. We sell some of the most beautiful clothes and toys available. We have recently started to do haircuts for kids and we need a flyer to promote this.
The design should be in line with the boutique nature of the shop, the care and attention we pay to each of our customers and lovely items we have for sale. This flyer is primarily to promote the availability of haircuts but will be circulated in the local area to also promote awareness of the shop which only opened a few months ago.

The flyer design should be double sided A5

One side should be all dark blue with just the logo with hair dryer and 'Tiny Brookvale' text with the text below:

Have your child's hair cut at our new salon just for little people! Call 0207 514 0627 or email shop@tinybrookvale.com to book an appointment.

Follow us on Chirply @tinybrookvale

We use the blue background logo and this blue should be the predominant color of the flyer.

Target Market(s)

Discerning parents, mid to high end consumers, high earners..

Industry/Entity Type

Shop

Font styles to use
Other font styles liked:
• Sa

Colors
3177b5
3377b5
85acd3
3076b4

Requirements
Must have
• It would be great to have generic shot of a kid having their haircut. A s hot without copy right issues please.
• Shot of hairdressing, show what the shop looks like.
• Sophisticated feel.
Should not have
• Not a cartoon feel

```html
<!DOCTYPE html>
<html lang="en">
<head>
<meta charset="utf-8">
<title>Tiny Brookvale – Haircuts Flyer</title>
<link rel="stylesheet" href="https://fonts.googleapis.com/css2?family=Open+Sans:wght@400;700;800&display=swap">
<style>
  :root {
    --flyer-blue: #3434b2;
    --flyer-blue-deep: #2a2a9e;
    --flyer-lilac: #c9c6e6;
    --cream: #f3ecd6;
    --white: #ffffff;
    --page: #ececef;
    --photo-warm-a: #c9a27e;
    --photo-warm-b: #7d5a45;
    --photo-shop-a: #d8c7c2;
    --photo-shop-b: #9a4048;
    --mascot-line: #e9e7f7;
  }
  * { box-sizing: border-box; margin: 0; padding: 0; }
  html, body { width: 1200px; height: 712px; overflow: hidden; }
  body {
    background: var(--page);
    font-family: "Open Sans", Arial, sans-serif;
    position: relative;
  }
  .flyer {
    position: absolute;
    top: 154px;
    width: 570px;
    height: 403px;
    overflow: hidden;
    box-shadow: 0 6px 18px rgba(0,0,0,.18);
  }
  /* Photo side */
  .flyer--photos {
    left: 20px;
    background: linear-gradient(180deg, var(--flyer-blue) 0%, var(--flyer-blue) 52%, var(--flyer-lilac) 100%);
  }
  .photo {
    position: absolute;
    border-radius: 50%;
    border: 6px solid rgba(255,255,255,.12);
  }
  .photo--smiling-child { left: 40px; top: 62px; width: 170px; height: 170px;
    background: radial-gradient(circle at 45% 45%, var(--photo-warm-a), var(--photo-warm-b)); }
  .photo--haircut { left: 368px; top: 18px; width: 170px; height: 170px;
    background: radial-gradient(circle at 55% 40%, #e3bfa0, #7a6050); }
  .photo--shop-rails { left: 252px; top: 150px; width: 126px; height: 126px;
    background: radial-gradient(circle at 50% 50%, var(--photo-shop-a), var(--photo-shop-b)); }
  .photo--shop-shelves { left: 395px; top: 203px; width: 140px; height: 140px;
    background: radial-gradient(circle at 50% 45%, #f1ece8, #b98c84); }
  .brand {
    position: absolute;
    left: 40px;
    top: 272px;
    display: flex;
    align-items: center;
    gap: 10px;
  }
  .brand__mark { width: 34px; height: 34px; background: var(--cream); border-radius: 50%; }
  .brand__name {
    font-weight: 800;
    font-size: 34px;
    line-height: 1;
    color: var(--cream);
    letter-spacing: -0.5px;
  }
  .flyer--photos .tagline {
    position: absolute;
    left: 40px;
    top: 348px;
    font-size: 9.5px;
    font-weight: 700;
    color: var(--flyer-blue-deep);
  }
  /* Contact side */
  .flyer--contact {
    left: 610px;
    background: var(--flyer-blue);
    color: var(--white);
  }
  .mascot {
    position: absolute;
    left: 30px;
    top: 20px;
    width: 290px;
    height: 383px;
    border-radius: 140px 140px 0 0;
    background: radial-gradient(ellipse at 50% 35%, rgba(233,231,247,.22), rgba(233,231,247,0) 70%);
  }
  .flyer--contact .brand__name {
    position: absolute;
    right: 34px;
    top: 130px;
    font-size: 58px;
    line-height: 0.95;
    text-align: right;
  }
  .flyer--contact .tagline {
    position: absolute;
    right: 18px;
    top: 262px;
    font-size: 10.5px;
    font-weight: 700;
  }
  .contact {
    position: absolute;
    right: 26px;
    top: 296px;
    width: 300px;
    font-size: 11px;
    line-height: 1.55;
    text-align: center;
  }
</style>
</head>
<body>
  <section class="flyer flyer--photos" aria-label="Flyer front">
    <div class="photo photo--smiling-child" role="img" aria-label="Photo of a smiling toddler in the salon chair"></div>
    <div class="photo photo--haircut" role="img" aria-label="Photo of a child having a haircut with scissors and comb"></div>
    <div class="photo photo--shop-rails" role="img" aria-label="Photo of clothing rails in the shop"></div>
    <div class="photo photo--shop-shelves" role="img" aria-label="Photo of shop shelves with toys and babywear"></div>
    <div class="brand">
      <span class="brand__mark" aria-hidden="true"></span>
      <span class="brand__name">Tiny Brookvale</span>
    </div>
    <p class="tagline">Have your child's hair cut at our new salon just for little people!</p>
  </section>

  <section class="flyer flyer--contact" aria-label="Flyer back">
    <div class="mascot" role="img" aria-label="Line illustration of the shop mascot holding a hair dryer"></div>
    <h1 class="brand__name">Tiny<br>Brookvale</h1>
    <p class="tagline">Have your child's hair cut at our new salon just for little people!</p>
    <p class="contact">
      Call: 0207 514 0627 or email: shop@tinybrookvale.com<br>
      to book an appointment.<br>
      Follow us on Chirply @tinybrookvale
    </p>
  </section>
</body>
</html>
```